Bref créative
Overseas Capital Partners
I need single sided standard sized Business Card [3.5" x 2"]
May be same as in logo, may be another
Professional
Marek Dobrzyn
Manager
ul. Lipowa 17
41-806 Katowice
Poland
marek.dobrzyn@korvant.com.pl
www.korvant.com.pl

```html
<!DOCTYPE html>
<html lang="en">
<head>
<meta charset="utf-8">
<title>Korvant business card</title>
<link rel="stylesheet" href="https://fonts.googleapis.com/css2?family=Arimo:wght@400;700&display=swap">
<style>
  :root {
    --brand-blue: #1ea3dd;
    --brand-blue-dark: #1590c8;
    --card-white: #ffffff;
    --backdrop: #e9e6e1;
    --rule: rgba(255,255,255,0.55);
    --text-light: #ffffff;
  }
  * { box-sizing: border-box; margin: 0; padding: 0; }
  html, body { width: 1200px; height: 744px; overflow: hidden; }
  body {
    background: var(--backdrop);
    font-family: "Arimo", Arial, sans-serif;
    position: relative;
  }
  .card {
    position: absolute;
    border-radius: 18px;
    overflow: hidden;
    background: var(--card-white);
    box-shadow: 0 6px 18px rgba(0,0,0,0.18);
  }
  .card-landscape { left: 86px; top: 194px; width: 624px; height: 357px; display: flex; }
  .card-portrait { left: 770px; top: 72px; width: 343px; height: 600px; display: flex; flex-direction: column; }

  .contact-panel { background: var(--brand-blue); color: var(--text-light); }
  .card-landscape .contact-panel { width: 46%; padding: 40px 30px 0 34px; }
  .card-portrait .contact-panel { height: 40%; padding: 30px 30px 0 34px; }

  .brand-panel { flex: 1; display: flex; align-items: center; justify-content: center; }
  .card-portrait .brand-panel { height: 60%; flex: none; }

  .wordmark { display: flex; align-items: center; gap: 12px; color: var(--brand-blue); font-weight: 400; letter-spacing: 8px; }
  .card-landscape .wordmark { font-size: 40px; }
  .card-portrait .wordmark { font-size: 38px; }
  .wordmark-square { width: 16px; height: 16px; background: var(--brand-blue); }

  .person-name { font-size: 21px; font-weight: 700; }
  .card-portrait .person-name { font-size: 19px; }
  .person-role { font-size: 13px; font-weight: 700; margin-top: 2px; }
  .rule { height: 1px; background: var(--rule); margin: 14px 0 12px; }
  .card-portrait .rule { margin: 10px 0 9px; }
  .contact-list { list-style: none; font-size: 12.5px; }
  .contact-list li { display: flex; align-items: center; gap: 8px; line-height: 21px; }
  .card-portrait .contact-list { font-size: 11.5px; }
  .card-portrait .contact-list li { line-height: 18px; }
  .contact-list svg { width: 13px; height: 13px; flex: none; }
  .address { font-size: 12.5px; line-height: 19px; }
  .card-portrait .address { font-size: 11.5px; line-height: 17px; }
</style>
</head>
<body>

<svg width="0" height="0" style="position:absolute">
  <defs>
    <symbol id="icon-phone" viewBox="0 0 14 14"><rect x="3.5" y="0.5" width="7" height="13" rx="1.5" fill="#fff"/><rect x="5" y="2.5" width="4" height="6" fill="#1ea3dd"/></symbol>
    <symbol id="icon-mail" viewBox="0 0 14 14"><rect x="0.5" y="2.5" width="13" height="9" rx="1" fill="#fff"/><path d="M1 3 L7 8 L13 3" stroke="#1ea3dd" stroke-width="1.2" fill="none"/></symbol>
    <symbol id="icon-web" viewBox="0 0 14 14"><circle cx="7" cy="7" r="6.2" fill="#fff"/><g stroke="#1ea3dd" stroke-width="0.9" fill="none"><ellipse cx="7" cy="7" rx="2.6" ry="6"/><line x1="1" y1="7" x2="13" y2="7"/></g></symbol>
  </defs>
</svg>

<section class="card card-landscape">
  <div class="contact-panel">
    <div class="person-name">Marek Dobrzyn</div>
    <div class="person-role">Manager</div>
    <div class="rule"></div>
    <ul class="contact-list">
      <li><svg><use href="#icon-phone"/></svg>+48 602 71 43 85</li>
      <li><svg><use href="#icon-mail"/></svg>marek.dobrzyn@korvant.com.pl</li>
      <li><svg><use href="#icon-web"/></svg>www.korvant.com.pl</li>
    </ul>
    <div class="rule"></div>
    <p class="address">ul. Lipowa 17<br>41-806 Katowice, Poland</p>
  </div>
  <div class="brand-panel">
    <div class="wordmark"><span class="wordmark-square"></span>KORVANT</div>
  </div>
</section>

<section class="card card-portrait">
  <div class="brand-panel">
    <div class="wordmark"><span class="wordmark-square"></span>KORVANT</div>
  </div>
  <div class="contact-panel">
    <div class="person-name">Marek Dobrzyn</div>
    <div class="person-role">Manager</div>
    <div class="rule"></div>
    <ul class="contact-list">
      <li><svg><use href="#icon-phone"/></svg>+48 602 71 43 85</li>
      <li><svg><use href="#icon-mail"/></svg>marek.dobrzyn@korvant.com.pl</li>
      <li><svg><use href="#icon-web"/></svg>www.korvant.com.pl</li>
    </ul>
    <div class="rule"></div>
    <p class="address">ul. Lipowa 17<br>41-806 Katowice, Poland</p>
  </div>
</section>

</body>
</html>
```